Wholistic Health Clinic (Chiropractic Osteopathic Naturapathic Homeopathic New Website Design

Create a beautiful website for Fenwick Chiropractic clinic that has been in the Sutherland Shire for over 40 years, that exemplifies the passion for helping people with their health goals using that may include a variety of techniques including Chiropractic, Osteopathy, Acupuncture, Applied Kinesiology, Retained Neonatal Reflexes, Nutritional Advice, Exercise Prescription, Decompression therapy, Massage and Stress management techniques.
We have a wholistic approach that includes Nutritional, Emotional and Physical health

(A more detailed draft will be supplied shortly)

Pages:
Home page
About Us Page
Team Page
Contact page
Terms of service Page
Privacy Page
and any other relevant page(s)

Will supply photos for:
- The Team Page and their qualifications & brief resume
- About Us page

Will supply logos for:
BPN
TORVEX
PLORIVEN
GRANTLEAF
MVA
KPO

Target Market(s)

main target Parents of young children and those 20's to 60's who live in the Sutherland Shire & have disposable income (that said almost everybody would benefit from their services)

Coding

Coded - Design and coding required

Number of Pages Required

5+ page

Font styles to use
Sans Serif

Requirements
Must have
• Please follow the brief

1. Easy to manage ourselves to add alerts (like Covid 19 compliance & Harbel week etc.) & update content like photos of team members etc.
2. Must be responsive and look good on mobile devices
3. must be fast loading
4. Logo on every page
5. Easy navigation on every page
6. Phone number must be clickable
7. Terms of service & Privacy pages
8. Slider on page 1 using photo of healthy people of all ages enjoying various lifestyles & ability to add other photos easily
Should not have
• no testimonials or any non compliant elements according to the BPN

```html
<!DOCTYPE html>
<html lang="en">
<head>
<meta charset="utf-8">
<title>Fenwick Chiropractic – Wholistic Health Clinic</title>
<link href="https://fonts.googleapis.com/css2?family=Poppins:wght@400;500;600&family=Open+Sans:wght@400;600&display=swap" rel="stylesheet">
<style>
:root{
  --green:#6fd03a;
  --green-dark:#4e9a2a;
  --green-light:#a9d48c;
  --ink:#111;
  --text:#555;
  --dark:#151515;
  --grey-bg:#f2f2f2;
  --white:#fff;
}
*{box-sizing:border-box;margin:0;padding:0}
html,body{width:1200px;height:3831px;overflow:hidden}
body{font-family:"Open Sans",sans-serif;color:var(--text);background:var(--white);position:relative}
.abs{position:absolute}
h1,h2,h3,h4,.btn,.nav a{font-family:"Poppins",sans-serif;font-weight:500}
.wrap{position:absolute;left:90px;width:1020px}

/* top bar */
.topbar{top:0;left:0;width:1200px;height:45px;background:var(--green-light);border-top:5px solid #222;font-size:14px;color:#222}
.topbar .addr{left:90px;top:12px;display:flex;align-items:center;gap:6px}
.topbar .follow{right:90px;top:12px;display:flex;align-items:center;gap:7px}
.sq{width:15px;height:15px;background:#222;border-radius:2px;display:inline-block}

/* header */
.header{top:45px;left:0;width:1200px;height:79px;background:var(--white)}
.brand{left:90px;top:22px;display:flex;align-items:center;gap:10px;font-family:"Poppins",sans-serif;color:#222}
.brand .dot{width:34px;height:34px;border-radius:50%;background:#222}
.brand b{display:block;font-size:16px;font-weight:500;line-height:1.1}
.brand small{display:block;font-size:9px;letter-spacing:.2px;text-transform:uppercase}
.contact{top:30px;right:90px;display:flex;gap:38px;font-size:16px;color:#333;align-items:center}
.contact span{display:flex;align-items:center;gap:12px}
.contact strong{font-weight:600;color:#111}

/* hero */
.hero{top:124px;left:0;width:1200px;height:582px;background:linear-gradient(135deg,#4b3a30 0%,#2d2520 40%,#6b584c 70%,#3a2f29 100%)}
.hero .shade{inset:0;background:rgba(0,0,0,.35)}
.nav{top:0;left:0;width:1200px;height:77px;background:rgba(30,30,30,.55)}
.nav ul{list-style:none;display:flex;gap:32px;position:absolute;left:92px;top:28px}
.nav a{color:var(--white);text-decoration:none;font-size:16px}
.nav a.active{color:var(--green)}
.btn{display:inline-block;background:var(--green);color:var(--white);text-decoration:none;text-align:center}
.nav .btn{position:absolute;right:90px;top:13px;width:247px;height:51px;line-height:51px;font-size:16px}
.hero-copy{top:185px;left:0;width:1200px;text-align:center;color:var(--white)}
.hero-copy h1{font-size:54px;font-weight:500;letter-spacing:.5px}
.hero-copy p{font-size:18px;line-height:28px;margin:14px auto 0;width:600px}
.hero-copy .btn{margin-top:16px;width:200px;height:52px;line-height:52px;font-size:20px}

/* info panel */
.panel{top:641px;left:89px;width:1021px;height:274px;background:var(--green);border-bottom:10px solid #111;color:var(--white);display:flex}
.panel .advice{width:493px;padding:34px 44px;border-right:1px solid rgba(255,255,255,.45)}
.panel h3{font-size:24px;line-height:39px;font-weight:500;display:flex;gap:10px}
.panel h3 svg{flex:none;margin-top:10px}
.panel .advice p{font-size:15px;line-height:27px;margin:14px 0 0}
.panel .advice .ghost{display:inline-block;margin-top:14px;border:1px solid var(--white);padding:8px 14px;font-size:14px;font-family:"Poppins",sans-serif;color:var(--white)}
.panel .hours{padding:22px 0 0 58px;flex:1}
.hours table{margin-top:24px;border-collapse:collapse;font-size:17px}
.hours td{height:41px}
.hours td:first-child{width:265px}
.hours td:last-child{font-size:14px}

/* welcome */
.welcome{top:998px;text-align:center}
.welcome h2,.section-title{font-size:42px;color:var(--ink);font-weight:500}
.lead{font-size:18px;line-height:33px;color:var(--text);margin-top:10px}
.features{top:1190px;left:89px;width:1021px;height:300px}
.feature{position:absolute;top:0;text-align:center;padding-top:17px}
.feature .icon{width:99px;height:99px;border-radius:50%;margin:0 auto;display:flex;align-items:center;justify-content:center;background:var(--white);box-shadow:0 2px 10px rgba(0,0,0,.15)}
.feature.on{background:var(--white);box-shadow:0 2px 14px rgba(0,0,0,.18);border-bottom:8px solid var(--green);height:302px}
.feature.on .icon{background:var(--green);box-shadow:none}
.feature h4{font-size:21px;color:#222;margin-top:30px}
.feature p{font-size:15px;line-height:28px;margin-top:8px;text-align:justify;text-align-last:center;padding:0 20px}
.dots{display:flex;gap:8px;position:absolute;left:576px}
.dots i{width:11px;height:11px;border-radius:50%;background:#111;display:block}
.dots i.g{background:var(--green)}

/* who we are */
.who{top:1651px;left:0;width:1200px;height:428px;background:linear-gradient(90deg,#0c0c0c,#1d1d1d 60%,#2a2622)}
.who h2{position:absolute;left:90px;top:44px;color:var(--white);font-size:38px;font-weight:500}
.who p{position:absolute;left:90px;top:111px;width:520px;color:var(--white);font-size:18px;line-height:36px}
.who .btn{position:absolute;left:90px;top:316px;width:213px;height:57px;line-height:57px;font-size:20px}
.who .photo{position:absolute;left:746px;top:37px;width:363px;height:353px;border:4px solid var(--white);background:linear-gradient(120deg,#c9b29c,#e8e2da 45%,#b9c9d8)}

/* what we do */
.do-head{top:2158px;text-align:center}
.services{top:2309px;left:89px;width:1021px;height:370px}
.svc{position:absolute;top:0;width:321px;background:var(--grey-bg);border:4px solid #fafafa;text-align:center}
.svc .img{width:100%}
.svc h4{font-size:22px;color:#222;font-weight:500}
.svc p{font-size:14px;line-height:27px;padding:6px 10px 0;text-align:justify;text-align-last:center}

/* partners */
.partners{top:2833px;left:0;width:1200px;height:346px;background:#f1f1f1}
.partners h2{position:absolute;top:30px;width:1200px;text-align:center;font-size:40px;color:var(--ink);font-weight:500}
.logo-box{position:absolute;top:116px;width:238px;height:141px;background:var(--white);box-shadow:2px 3px 5px rgba(0,0,0,.2);display:flex;align-items:center;justify-content:center;gap:10px;font-family:"Poppins",sans-serif;font-weight:600;font-size:30px;color:#1d3f8f}

/* newsletter */
.news{top:3262px;text-align:center}
.field{top:3355px;left:208px;width:552px;height:70px;border:2px solid #333;display:flex;align-items:center;gap:14px;padding-left:24px;font-size:19px;color:#444}
.subscribe{top:3355px;left:807px;width:245px;height:70px;line-height:70px;font-size:22px}

/* footer */
.footer{top:3506px;left:0;width:1200px;height:325px;background:var(--dark);color:var(--white)}
.footer .brand{top:33px;left:90px;color:var(--white)}
.footer .brand .dot{width:60px;height:60px;background:var(--white)}
.footer .brand b{font-size:22px;font-weight:400}
.footer .brand small{font-size:13px}
.footer .about{position:absolute;left:90px;top:125px;width:330px;font-size:16px;line-height:28px;text-align:justify}
.fcol{position:absolute;top:62px}
.fcol h5{font-family:"Poppins",sans-serif;font-size:17px;font-weight:500;margin-bottom:14px}
.fcol li{list-style:none;font-size:16px;line-height:32.5px}
.copy{position:absolute;top:268px;width:1200px;text-align:center;font-size:16px}
</style>
</head>
<body>

<div class="abs topbar">
  <div class="abs addr">
    <svg width="10" height="14" viewBox="0 0 10 14"><path d="M5 0a5 5 0 0 0-5 5c0 4 5 9 5 9s5-5 5-9a5 5 0 0 0-5-5zm0 7a2 2 0 1 1 0-4 2 2 0 0 1 0 4z" fill="#222"/></svg>
    27 LARKMOOR RD WENHOLT BAY NSW 2990
  </div>
  <div class="abs follow">FOLLOW US: <span class="sq"></span><span class="sq"></span><span class="sq"></span></div>
</div>

<header class="abs header">
  <div class="abs brand"><span class="dot"></span><div><b>Fenwick Chiropractic</b><small>Wholistic Health Clinic</small></div></div>
  <div class="abs contact">
    <span><svg width="18" height="14" viewBox="0 0 18 14"><rect x="1" y="1" width="16" height="12" fill="none" stroke="#333" stroke-width="1.6"/><path d="M1 1l8 7 8-7" fill="none" stroke="#333" stroke-width="1.6"/></svg>Send Message contact@fenwickchiro.example</span>
    <span><svg width="16" height="16" viewBox="0 0 16 16"><path d="M3 1l3 3-2 2c1 2 3 4 5 5l2-2 3 3-2 3C6 15 1 10 1 3z" fill="#333"/></svg>Hot Line <strong>1-555-010-4821</strong></span>
  </div>
</header>

<section class="abs hero" role="img" aria-label="Photo of a smiling family of parents and children together">
  <div class="abs shade"></div>
  <nav class="abs nav">
    <ul><li><a class="active" href="#">HOME</a></li><li><a href="#">ABOUT US</a></li><li><a href="#">TEAM</a></li><li><a href="#">CONTACT US</a></li></ul>
    <a class="btn" href="#">MAKE AN APPTOINTMENT</a>
  </nav>
  <div class="abs hero-copy">
    <h1>FENWICK CHIROPRACTIC</h1>
    <p>Fenwick Chiropractic, situated in Wenholt and established for 40 years, is passionate about helping you achieve your vitality</p>
    <a class="btn" href="#">GET STARTED</a>
  </div>
</section>

<div class="abs panel">
  <div class="advice">
    <h3><svg width="20" height="20" viewBox="0 0 20 20"><rect x="1" y="4" width="14" height="14" fill="none" stroke="#fff" stroke-width="2"/><path d="M8 12l9-9 2 2-9 9H8z" fill="#fff"/></svg>NEED ADVICE AND SOME PHYSICAL THERAPY ADVISES</h3>
    <p>Our clinics Chiropractic procedures are extremely safe and gentle and can be applied to all phases of life for optimum health</p>
    <span class="ghost">GET AN APPOINTMENT</span>
  </div>
  <div class="hours">
    <h3><svg width="20" height="20" viewBox="0 0 20 20"><circle cx="10" cy="10" r="8" fill="none" stroke="#fff" stroke-width="2.2"/><path d="M10 5v6h4" fill="none" stroke="#fff" stroke-width="2.2"/></svg>OPENING HOURS</h3>
    <table>
      <tr><td>MONDAY &amp; FRIDAY</td><td>9 - 12 AM , 1:30 - 6:30 PM</td></tr>
      <tr><td>WEDNESDAY</td><td>8 AM - 7 PM</td></tr>
      <tr><td>TUESDAY &amp; THURSDAY</td><td>2:30 - 6:30 PM</td></tr>
      <tr><td>SATURDAY</td><td>8 AM - 1 PM</td></tr>
    </table>
  </div>
</div>

<section class="wrap welcome">
  <h2>WELCOME TO THE FENWICK CHIROPRACTIC</h2>
  <p class="lead">Our clinics Chiropractic procedures are extremely safe and gentle and can be applied to all<br>phases of life for optimum health</p>
</section>

<div class="abs features">
  <div class="feature" style="left:0;width:305px">
    <div class="icon"><svg width="60" height="50" viewBox="0 0 60 50" fill="none" stroke="#6fd03a" stroke-width="2.4"><circle cx="12" cy="10" r="6"/><circle cx="30" cy="10" r="6"/><circle cx="48" cy="10" r="6"/><path d="M4 46V26q8-8 16 0v20M22 46V26q8-8 16 0v20M40 46V26q8-8 16 0v20"/></svg></div>
    <h4>HAPPY BALANCED KIDS</h4>
    <p>Lorem ipsum dolor sit amet, consectetur adipiscing elit, sed do eiusmod tempor incididunt ut labore et dolore magna aliqua.</p>
  </div>
  <div class="feature on" style="left:357px;width:318px">
    <div class="icon"><svg width="50" height="56" viewBox="0 0 50 56" fill="none" stroke="#fff" stroke-width="2.4"><circle cx="25" cy="12" r="8"/><path d="M10 54V34q15-14 30 0v20M25 26v28"/></svg></div>
    <h4>HEALTHY BODIES</h4>
    <p>We focus on establishing the best nervous system function to improve learning, behavior, muscle function, strength and posture</p>
  </div>
  <div class="feature" style="left:733px;width:288px">
    <div class="icon"><svg width="64" height="64" viewBox="0 0 64 64" fill="none" stroke="#6fd03a" stroke-width="3"><circle cx="32" cy="34" r="24" stroke-dasharray="5 5"/><path d="M32 20v14l10 6"/><path d="M30 6l6 4-6 4"/></svg></div>
    <h4>IMPROVED PERFORMANCE</h4>
    <p>Lorem ipsum dolor sit amet, consectetur adipiscing elit, sed do eiusmod tempor incididunt ut labore et dolore magna aliqua.</p>
  </div>
</div>
<div class="dots" style="top:1546px"><i></i><i class="g"></i><i></i></div>

<section class="abs who">
  <h2>WHO WE ARE</h2>
  <p>Fenwick Chiropractic, situated in Wenholt and established for 40 years, is passionate about helping you achieve your vitality and regain your health. We use a unique wholistic approach, understand you are an individual and tailor your treatment accordingly.We understand your health may be affected</p>
  <a class="btn" href="#">READ MORE</a>
  <div class="photo" role="img" aria-label="Photo of a chiropractor explaining a spine model to a patient"></div>
</section>

<section class="wrap do-head">
  <h2 class="section-title">WHAT WE DO</h2>
  <p class="lead">Our clinics Chiropractic procedures are extremely safe and gentle and can be applied to all phases of life<br>for optimum health, from the newborn to the elderly.</p>
</section>

<div class="abs services">
  <div class="svc" style="left:0;height:368px;border-bottom:5px solid var(--green)">
    <div class="img" role="img" aria-label="Photo of a chiropractor adjusting a patient's back" style="height:144px;background:linear-gradient(120deg,#d8d3cc,#8a7a6c 55%,#eae6e0)"></div>
    <h4 style="margin-top:22px">CHIROPRACTIC</h4>
    <p>All bodily function is controlled by the brain through the nervous system.The moving bones of the skull, spine and pelvis protect the delicate nerve tissue of the brain and spinal cord, yet allows flexibility</p>
  </div>
  <div class="svc" style="left:353px;height:368px;border-bottom:5px solid var(--green-dark)">
    <div class="img" role="img" aria-label="Photo of pink kinesiology tape applied to a knee" style="height:299px;background:linear-gradient(135deg,#c99a80,#e86aa0 50%,#b58670)"></div>
    <h4 style="margin-top:22px">APPLIED KINESIOLOGY</h4>
  </div>
  <div class="svc" style="left:699px;height:368px;border-bottom:5px solid #111">
    <div class="img" role="img" aria-label="Photo of acupuncture needles in a patient's back" style="height:299px;background:linear-gradient(135deg,#d9a58a,#b97860 55%,#e4c2ae)"></div>
    <h4 style="margin-top:22px">ACUPUNCTURE</h4>
  </div>
</div>
<div class="dots" style="top:2728px"><i></i><i class="g"></i><i></i></div>

<section class="abs partners">
  <h2>PARTNERS</h2>
  <div class="logo-box" style="left:89px">BPN</div>
  <div class="logo-box" style="left:348px">TORVEX</div>
  <div class="logo-box" style="left:608px">PLORIVEN</div>
  <div class="logo-box" style="left:868px;font-size:24px">Tarlow Solutions</div>
  <div class="dots" style="top:302px;left:574px"><i></i><i class="g"></i><i></i></div>
</section>

<section class="wrap news">
  <h2 class="section-title">NEWSLETTER SIGN UP</h2>
</section>
<div class="abs field">
  <svg width="28" height="20" viewBox="0 0 28 20"><rect x="1" y="1" width="26" height="18" rx="2" fill="none" stroke="#333" stroke-width="2"/><path d="M1 2l13 10 13-10" fill="none" stroke="#333" stroke-width="2"/></svg>
  Enter your email address
</div>
<a class="abs btn subscribe" href="#">SUBSCRIBE</a>

<footer class="abs footer">
  <div class="abs brand"><span class="dot"></span><div><b>Fenwick Chiropractic</b><small>Wholistic Health Clinic</small></div></div>
  <p class="about">We understand your health may be affected by structural, biochemical or emotional factors and address these issues in your tailored care plan.</p>
  <div class="fcol" style="left:468px"><h5>QUICKS LINKS</h5><ul><li>Home</li><li>About Us</li><li>Team</li><li>Contact Us</li></ul></div>
  <div class="fcol" style="left:657px"><h5>SERVICES</h5><ul><li>Chiropractic</li><li>Osteopathy</li><li>Acupuncture</li><li>Nutritional Advice</li></ul></div>
  <div class="fcol" style="left:853px"><h5>CONATCT US</h5><ul><li>27 Larkmoor Rd</li><li>WENHOLT BAY NSW 2990</li><li>(02) 5550 1942</li><li>contact@fenwickchiro.example</li></ul></div>
  <p class="copy">Copyright © 2020 Fenwick Chiropractic .Terms of service | Privacy .All Rights Reserved</p>
</footer>

</body>
</html>
```